Business Card Design for Occupational Medicine Start Up Company

We need to design a professional business card. We are a healthcare company providing occupational medicine services to blue collar industries. We are professional, efficient and high quality service providers.

Target Market(s)

Blue Collar Industry: Shipbuilding, Ports, Trucking Companies; The Executives and Safety Officers for these companies

Industry/Entity Type

Healthcare

Contact Information for Business Card

Logo, Name, Title, Email, Phone

Other font styles liked:
• Please match our Brand Guide

Requirements
Must have
• Our Company Colors and Logo

```html
<!DOCTYPE html>
<html lang="en">
<head>
<meta charset="utf-8">
<title>Crewline Clinics — Business Card</title>
<link href="https://fonts.googleapis.com/css2?family=Montserrat:wght@400;500;700;800&display=swap" rel="stylesheet">
<style>
  :root {
    --backdrop: #e6e6e8;
    --amber: #f3b345;
    --navy: #2b2d77;
    --white: #ffffff;
    --card-w: 520px;
    --card-h: 297px;
    --radius: 26px;
  }
  * { box-sizing: border-box; margin: 0; padding: 0; }
  html, body {
    width: 1200px;
    height: 846px;
    overflow: hidden;
    background: var(--backdrop);
    font-family: "Montserrat", sans-serif;
  }
  .sheet {
    width: 1200px;
    height: 846px;
    display: flex;
    align-items: center;
    justify-content: center;
    gap: 40px;
  }
  .card {
    width: var(--card-w);
    height: var(--card-h);
    border-radius: var(--radius);
    position: relative;
    overflow: hidden;
  }

  /* Contact side */
  .card--contact {
    background: var(--amber);
    color: var(--navy);
    display: flex;
    align-items: center;
  }
  .card--contact .brand-mark {
    width: 44%;
    display: flex;
    flex-direction: column;
    align-items: center;
    gap: 10px;
  }
  .brand-mark__dot {
    width: 46px;
    height: 46px;
    border-radius: 50%;
    background: var(--navy);
  }
  .brand-mark__name {
    font-weight: 800;
    font-size: 17px;
    letter-spacing: 1.5px;
    color: var(--navy);
  }
  .details { display: flex; flex-direction: column; }
  .details__name {
    font-weight: 800;
    font-size: 21px;
    letter-spacing: 0.5px;
    line-height: 1.05;
  }
  .details__title {
    font-weight: 700;
    font-size: 14px;
    margin-left: 8px;
    margin-bottom: 22px;
  }
  .contact-list { list-style: none; display: flex; flex-direction: column; gap: 7px; }
  .contact-list li {
    display: flex;
    align-items: center;
    gap: 10px;
    font-size: 13px;
    font-weight: 500;
  }
  .contact-list svg { width: 15px; height: 15px; flex: none; fill: var(--navy); }
  .contact-list .is-caps { letter-spacing: 0.6px; }

  /* Brand side */
  .card--brand {
    background: var(--navy);
    color: var(--white);
    display: flex;
    flex-direction: column;
    align-items: center;
    justify-content: center;
    gap: 14px;
  }
  .card--brand .brand-mark__dot {
    width: 62px;
    height: 62px;
    background: var(--amber);
  }
  .wordmark { text-align: center; }
  .wordmark__primary {
    font-weight: 700;
    font-size: 34px;
    letter-spacing: 1px;
    line-height: 1;
  }
  .wordmark__secondary {
    font-weight: 700;
    font-size: 16px;
    letter-spacing: 12px;
    margin-top: 8px;
    padding-left: 12px;
  }
</style>
</head>
<body>
<main class="sheet">
  <section class="card card--contact">
    <div class="brand-mark">
      <span class="brand-mark__dot"></span>
      <span class="brand-mark__name">CREWLINE</span>
    </div>
    <div class="details">
      <p class="details__name">FULL NAME</p>
      <p class="details__title">Title</p>
      <ul class="contact-list">
        <li>
          <svg viewBox="0 0 24 24" aria-hidden="true"><path d="M6.6 10.8a15.1 15.1 0 0 0 6.6 6.6l2.2-2.2c.3-.3.7-.4 1-.2 1.1.4 2.3.6 3.6.6.6 0 1 .4 1 1V20c0 .6-.4 1-1 1A17 17 0 0 1 3 4c0-.6.4-1 1-1h3.5c.6 0 1 .4 1 1 0 1.3.2 2.5.6 3.6.1.3 0 .7-.2 1z"/></svg>
          <span>123-456-7890</span>
        </li>
        <li>
          <svg viewBox="0 0 24 24" aria-hidden="true"><path d="M2 5h20v14H2zM4 7v.4l8 5.3 8-5.3V7zm0 2.8V17h16V9.8l-8 5.3z"/></svg>
          <span>full.name@crewlineclinics.com</span>
        </li>
        <li>
          <svg viewBox="0 0 24 24" aria-hidden="true"><path d="M12 2a10 10 0 1 0 0 20 10 10 0 0 0 0-20zm6.9 6h-3a15 15 0 0 0-1.3-3.9A8 8 0 0 1 18.9 8zM12 4c.8 1.2 1.5 2.5 1.9 4h-3.8c.4-1.5 1.1-2.8 1.9-4zM4.3 14a8 8 0 0 1 0-4h3.4a16 16 0 0 0 0 4zm.8 2h3a15 15 0 0 0 1.3 3.9A8 8 0 0 1 5.1 16zm3-8h-3a8 8 0 0 1 4.3-3.9A15 15 0 0 0 8.1 8zM12 20c-.8-1.2-1.5-2.5-1.9-4h3.8c-.4 1.5-1.1 2.8-1.9 4zm2.3-6H9.7a14 14 0 0 1 0-4h4.6a14 14 0 0 1 0 4zm.3 5.9a15 15 0 0 0 1.3-3.9h3a8 8 0 0 1-4.3 3.9zm1.7-5.9a16 16 0 0 0 0-4h3.4a8 8 0 0 1 0 4z"/></svg>
          <span class="is-caps">CREWLINECLINICS.COM</span>
        </li>
      </ul>
    </div>
  </section>

  <section class="card card--brand">
    <span class="brand-mark__dot"></span>
    <div class="wordmark">
      <p class="wordmark__primary">CREWLINE</p>
      <p class="wordmark__secondary">CLINICS</p>
    </div>
  </section>
</main>
</body>
</html>
```